FungaVita Nutrition Require Label Design Assistance

We are FungaVita!

We are a new mushroom focused nutrition supplement company looking for some design assistance. We are looking to provide some of the highest quality mushroom supplements available on the market today, using 100% fruiting bodies where many other companies opt for cheaper alternatives. We strongly believe in the power of mushroom nutrition and wish to focus on the high-end supplement market.

We are starting with three initial ranges; Lions Mane, Turkey Tail and Reishi - and wish to have powerful yet elegant designs for each. We wish to be visually appealing whilst maintaining the high-end feel. Imagery of the mushrooms on the label would be good if it maintains high-end appeal. Our bottles will be dark green and lids will be white if this helps with visualization. We have a logo and preferred font for the name which can be used if possible. The image in the logo may need resizing to fit with the supplement market (smaller logo/larger font). If you provide a superior logo to that which we currently have, we would consider using it.

The three range designs should be the same, but with the mushroom name and any imagery changed to reflect the different ranges. I am happy to supply images where required.

Label dimensions = 55mm x 150mm

Target Market(s)

Premium High End Health Supplements

Industry/Entity Type

Supplement

Font styles to use
Serif
Sans Serif

Colors

Designer to choose colors to be used in the design.

Requirements
Must have
• Must have the text "100% Fruiting Bodies"
• Must have Organic + Vegan notification.
• Must have an ingredients section, and there will need to be some space for small-print (which will be decided on shortly).
Nice to have
• See label specifications in message thread.

```html
<!DOCTYPE html>
<html lang="en">
<head>
<meta charset="utf-8">
<title>FungaVita Supplement Labels</title>
<link href="https://fonts.googleapis.com/css2?family=Crimson+Text:wght@400;600&display=swap" rel="stylesheet">
<style>
  :root {
    --backdrop: #475857;
    --lime: #86ff00;
    --forest: #197a09;
    --ink-green: #1c6f0d;
    --warn-red: #e8231c;
    --paper: #ffffff;
    --cap-rim: #f2f2f2;
    --brand-ink: #2b2b2b;
  }
  * { margin: 0; padding: 0; box-sizing: border-box; }
  html, body { width: 1200px; height: 885px; overflow: hidden; }
  body { background: var(--backdrop); font-family: "Crimson Text", Georgia, serif; position: relative; }

  .label { position: absolute; left: 304px; width: 606px; height: 222px; background: var(--paper); overflow: hidden; }
  .label--lions { top: 79px; }
  .label--turkey { top: 326px; }
  .label--reishi { top: 576px; }

  .label-art { position: absolute; inset: 0; width: 606px; height: 222px; }
  .band-lime { fill: var(--lime); }
  .band-forest { fill: var(--forest); }
  .cap-frame { stroke: var(--cap-rim); stroke-width: 9; paint-order: stroke; stroke-linejoin: round; }
  .badge-disc { fill: var(--forest); }
  .badge-ring { fill: none; stroke: var(--paper); stroke-width: 1.5; }

  .brand { position: absolute; top: 123px; left: 0; width: 622px; text-align: center;
    font-size: 7.5px; letter-spacing: 1.2px; text-transform: uppercase; color: var(--brand-ink); }
  .product-name { position: absolute; top: 134px; left: 0; width: 622px; text-align: center;
    font-size: 24px; letter-spacing: 1.5px; color: var(--lime); font-weight: 400; line-height: 1; }
  .claim { position: absolute; top: 162px; left: 0; width: 622px; text-align: center;
    font-size: 13px; letter-spacing: 0.8px; color: var(--ink-green); line-height: 1; }
  .count { position: absolute; top: 194px; left: 0; width: 622px; text-align: center;
    color: var(--lime); line-height: 1; letter-spacing: 0.5px; }
  .count-number { font-size: 13px; }
  .count-unit { font-size: 9.5px; }

  .warnings { position: absolute; left: 8px; top: 163px; width: 178px; font-size: 8px; line-height: 9.1px; color: var(--ink-green); }
  .warnings-title { color: var(--warn-red); }

  .ingredients { position: absolute; left: 450px; width: 151px; border-collapse: collapse;
    border: 1.6px solid var(--forest); font-size: 9.6px; line-height: 11.5px; color: var(--ink-green); letter-spacing: 0.4px; }
  .ingredients td { border-top: 1.6px solid var(--forest); padding: 0 2px 1px 3px; vertical-align: top; }
  .ingredients tr:first-child td { border-top: none; }
  .ingredients .amount { text-align: right; white-space: nowrap; }
  .label--lions .ingredients, .label--reishi .ingredients { top: 167px; }
  .label--turkey .ingredients { top: 154px; }
</style>
</head>
<body>

<section class="label label--lions">
  <svg class="label-art" viewBox="0 0 606 222" aria-hidden="false">
    <defs>
      <linearGradient id="lionsTone" x1="0" y1="0" x2="1" y2="0">
        <stop offset="0" stop-color="#5f7a23"/>
        <stop offset="0.5" stop-color="#c9a77a"/>
        <stop offset="1" stop-color="#4f5a1c"/>
      </linearGradient>
    </defs>
    <path class="band-forest" d="M0 0 H606 V60 C560 62 480 44 400 28 C360 21 330 19 300 20 C230 24 120 50 0 86 Z"/>
    <path class="band-lime" d="M0 0 H606 V53 C560 58 480 40 400 24 C360 17 330 15 300 16 C230 20 120 44 0 77 Z"/>
    <path class="cap-frame" role="img" aria-label="Photo of layered tan bracket mushrooms on green moss" fill="url(#lionsTone)"
      d="M236 102 C250 62 288 34 318 34 C348 34 388 62 402 102 C370 90 272 88 236 102 Z"/>
    <circle class="badge-disc" cx="580" cy="143" r="19"/>
    <circle class="badge-ring" cx="580" cy="143" r="9"/>
    <rect class="band-lime" x="0" y="215" width="606" height="7"/>
  </svg>
  <div class="brand">FungaVita</div>
  <h1 class="product-name">Lions Mane</h1>
  <p class="claim">%100 Fruiting Bodies</p>
  <p class="count"><span class="count-number">60</span><span class="count-unit">capsule</span></p>
  <p class="warnings"><span class="warnings-title">Warnings:</span><br>Do not exceed stated recommended dose.A food supplement should not be used as a substitute for a varied diet. Store in a cool place, out of reach and sight of children.</p>
  <table class="ingredients">
    <tr><td>Lions Mane Organic<br>Fruiting Bodies</td><td class="amount">700mg</td></tr>
    <tr><td>Ginko Bilbao</td><td class="amount">35mg</td></tr>
  </table>
</section>

<section class="label label--turkey">
  <svg class="label-art" viewBox="0 0 606 222">
    <defs>
      <linearGradient id="turkeyTone" x1="0" y1="0" x2="1" y2="1">
        <stop offset="0" stop-color="#b06556"/>
        <stop offset="0.55" stop-color="#8a3a2c"/>
        <stop offset="1" stop-color="#5a2418"/>
      </linearGradient>
    </defs>
    <path class="band-forest" d="M0 0 H606 V60 C560 62 480 44 400 28 C360 21 330 19 300 20 C230 24 120 50 0 86 Z"/>
    <path class="band-lime" d="M0 0 H606 V53 C560 58 480 40 400 24 C360 17 330 15 300 16 C230 20 120 44 0 77 Z"/>
    <path class="cap-frame" role="img" aria-label="Photo of glossy red-brown shelf mushrooms" fill="url(#turkeyTone)"
      d="M234 108 C250 66 288 37 318 37 C350 37 392 66 406 108 C372 96 270 94 234 108 Z"/>
    <circle class="badge-disc" cx="580" cy="132" r="19"/>
    <circle class="badge-ring" cx="580" cy="132" r="9"/>
    <rect class="band-lime" x="0" y="215" width="606" height="7"/>
  </svg>
  <div class="brand">FungaVita</div>
  <h1 class="product-name">TURKEY TAIL</h1>
  <p class="claim">%100 Fruiting Bodies</p>
  <p class="count"><span class="count-number">60</span><span class="count-unit">capsule</span></p>
  <p class="warnings"><span class="warnings-title">Warnings:</span><br>Do not exceed stated recommended dose.A food supplement should not be used as a substitute for a varied diet. Store in a cool place, out of reach and sight of children.</p>
  <table class="ingredients">
    <tr><td>Turkey Tail Organic<br>Fruiting Bodies</td><td class="amount">600mg</td></tr>
    <tr><td>Organic Enoki Extract</td><td class="amount">25mg</td></tr>
    <tr><td>Curcumin</td><td class="amount">100mg</td></tr>
  </table>
</section>

<section class="label label--reishi">
  <svg class="label-art" viewBox="0 0 606 222">
    <defs>
      <linearGradient id="reishiTone" x1="0" y1="0" x2="1" y2="0">
        <stop offset="0" stop-color="#2d3a2a"/>
        <stop offset="0.35" stop-color="#dfe6ee"/>
        <stop offset="0.7" stop-color="#c9d3de"/>
        <stop offset="1" stop-color="#2a3626"/>
      </linearGradient>
    </defs>
    <path class="band-forest" d="M0 0 H606 V60 C560 62 480 44 400 28 C360 21 330 19 300 20 C230 24 120 50 0 86 Z"/>
    <path class="band-lime" d="M0 0 H606 V53 C560 58 480 40 400 24 C360 17 330 15 300 16 C230 20 120 44 0 77 Z"/>
    <path class="cap-frame" role="img" aria-label="Photo of a white icicle-like mushroom on dark woodland" fill="url(#reishiTone)"
      d="M236 102 C250 62 288 34 318 34 C348 34 388 62 402 102 C370 90 272 88 236 102 Z"/>
    <circle class="badge-disc" cx="580" cy="140" r="19"/>
    <circle class="badge-ring" cx="580" cy="140" r="9"/>
    <rect class="band-lime" x="0" y="215" width="606" height="7"/>
  </svg>
  <div class="brand">FungaVita</div>
  <h1 class="product-name">REISHI</h1>
  <p class="claim">%100 Fruiting Bodies</p>
  <p class="count"><span class="count-number">60</span><span class="count-unit">capsule</span></p>
  <p class="warnings"><span class="warnings-title">Warnings:</span><br>Do not exceed stated recommended dose.A food supplement should not be used as a substitute for a varied diet. Store in a cool place, out of reach and sight of children.</p>
  <table class="ingredients">
    <tr><td>Reishi Organic<br>Fruiting Bodies</td><td class="amount">700mg</td></tr>
    <tr><td>Green Tea Powder</td><td class="amount">35mg</td></tr>
  </table>
</section>

</body>
</html>
```